Remodeling brochure

We need an informative homeowner friendly brochure detailing our company and things we do. We are looking for an initial setup and ideas (# of pages, etc) and then we will send more content. We are uploading our logo design. We are a high end remodeling company specializing in kitchen & bath remodels. We sell ourselves on customer communication and attention to detail in our designs and remodels.

Target Market(s)

Residential homeowners

Contact Information for Business Card

Modern and attention grabbing

Requirements
Must have
• Name- Hearth & Tile Crafters<br/>Address- 728 NW Folley Lane Suite #217<br/> Ankeny, Iowa 50388<br/>Phone- 515-472-8093<br/>email-htcrafterspro@mailvane.net

```html
<!DOCTYPE html>
<html lang="en">
<head>
<meta charset="utf-8">
<title>Hearth &amp; Tile Crafters – Remodeling Brochure</title>
<link rel="stylesheet" href="https://fonts.googleapis.com/css2?family=Anton&family=Montserrat:wght@400;500;600;700&family=Saira+Semi+Condensed:wght@400;700&display=swap">
<style>
:root{
  --stage:#a6a6a6;
  --paper:#ffffff;
  --blue:#2a8bd2;
  --blue-deep:#1566c2;
  --navy:#3c56b0;
  --ink:#1b1b1b;
  --muted:#3a3a3a;
  --photo-kitchen:#6f6f6c;
  --photo-light:#d9dbdc;
}
*{margin:0;padding:0;box-sizing:border-box}
html,body{width:1200px;height:3548px;overflow:hidden}
body{background:var(--stage);position:relative;font-family:"Montserrat",sans-serif;color:var(--ink)}
.abs{position:absolute}
.page{position:absolute;background:var(--paper)}
.photo{position:absolute}
.cover-band{left:223px;top:117px;width:430px;height:149px;background:linear-gradient(90deg,var(--blue-deep),#1c7ad4);color:#fff;padding:16px 0 0 38px;font-family:"Saira Semi Condensed",sans-serif}
.cover-band .small{font-size:30px;letter-spacing:2px;line-height:1}
.cover-band .big{font-size:50px;font-weight:700;line-height:1.05}
.brand{display:flex;align-items:center;gap:12px}
.brand .mark{width:44px;height:44px;background:var(--blue-deep)}
.brand .name{font-family:"Montserrat",sans-serif;font-weight:700;color:var(--blue-deep);font-size:26px}
.toc{position:absolute;right:0;text-align:right;color:#fff}
.toc .num{font-family:"Anton",sans-serif;font-size:30px;line-height:1}
.toc .label{font-size:19px;font-weight:500;margin-top:10px}
.anton{font-family:"Anton",sans-serif}
.body-copy{font-size:10px;line-height:1.55;font-weight:500;color:var(--muted)}
.rule{position:absolute;height:2px;background:#9fc6e8}
.rule .accent{position:absolute;right:0;top:-1px;height:4px;background:var(--blue)}
.tag{font-size:11px;font-weight:700}
</style>
</head>
<body>

<!-- Cover -->
<section class="page" style="left:229px;top:51px;width:733px;height:949px">
  <div class="photo" role="img" aria-label="Photo of a modern kitchen with patterned tile backsplash, dark cabinets and white bar stools" style="left:18px;top:18px;width:697px;height:718px;background:linear-gradient(180deg,#cfcfcd 0%,#8b8b88 35%,#4b4c4d 70%,#3a3836 100%)"></div>
  <div class="abs" style="left:206px;top:748px;width:509px;height:182px;background:linear-gradient(90deg,#ffffff,#ededed)"></div>
  <div class="abs brand" style="left:363px;top:800px">
    <div class="mark"></div>
    <div class="name">HEARTH &amp; TILE CRAFTERS</div>
  </div>
</section>
<div class="abs cover-band">
  <div class="small">Specializing in</div>
  <div class="big">KITCHEN &amp; BATH</div>
  <div class="small" style="font-size:29px">Remodels</div>
</div>

<!-- Spread: contents / welcome -->
<section class="page" style="left:90px;top:1053px;width:1004px;height:704px">
  <div class="abs" style="left:5px;top:5px;width:576px;height:692px;background:var(--blue)"></div>
  <div class="abs" style="left:351px;top:216px;width:230px;height:425px;background:#fff"></div>
  <div class="photo" role="img" aria-label="Photo of a grey shaker-style kitchen with white countertops" style="left:581px;top:5px;width:346px;height:211px;background:linear-gradient(180deg,#e8e8e6,#7a7b7c 60%,#55565a)"></div>
  <div class="abs" style="left:939px;top:5px;width:58px;height:211px;background:var(--blue)"></div>
  <div class="abs" style="left:5px;top:0;width:298px;height:704px">
    <div class="toc" style="top:137px"><div class="num">01</div><div class="label">Title Goes Here</div></div>
    <div class="toc" style="top:239px"><div class="num">02</div><div class="label">Another Title Here</div></div>
    <div class="toc" style="top:348px"><div class="num">03</div><div class="label">Page Headline Here</div></div>
    <div class="toc" style="top:448px"><div class="num">04</div><div class="label">Headline Here</div></div>
    <div class="toc" style="top:557px"><div class="num">05</div><div class="label">Another Headline</div></div>
  </div>
  <div class="abs anton" style="left:378px;top:610px;font-size:62px;transform:rotate(-90deg);transform-origin:left top;color:var(--ink);line-height:1">CONTENT</div>
  <div class="abs" style="left:581px;top:264px;font-size:19px;font-weight:500">Welcome To</div>
  <div class="abs anton" style="left:581px;top:294px;font-size:48px;line-height:1.1">COMPANY</div>
  <div class="abs" style="left:658px;top:384px;width:7px;height:40px;background:var(--ink)"></div>
  <div class="abs body-copy" style="left:684px;top:385px;width:260px;color:#222">Lorem ipsum dolor sit amet, consectetur adipiscing elit. Sed molestie luctus est, quis malesuada purus volutpat nec. Sed fermentum tellus rhoncus lacus venenatis pellentesque. Vivamus nisl augue, lacinia sit amet augue sit amet, scelerisque porta elit. Aliquam erat volutpat.</div>
  <div class="abs body-copy" style="left:684px;top:517px;width:260px;color:#222">Donec pretium, tortor et laoreet cursus, magna magna interdum nulla, in aliquet tellus orci sit amet justo. Nullam justo nisl, semper ut lacinia at, tristique at purus. Quisque rhoncus odio a egestas vestibulum.</div>
</section>

<!-- Spread: vision -->
<section class="page" style="left:90px;top:1896px;width:1004px;height:704px">
  <div class="photo" role="img" aria-label="Photo of a bright bathroom with double vanity, dark cabinets, round mirrors and a freestanding tub" style="left:0;top:58px;width:540px;height:593px;background:linear-gradient(180deg,#eeeeec 0%,#d8d9da 45%,#5d6066 75%,#4b4e54 100%)"></div>
  <div class="rule" style="left:558px;top:44px;width:323px"><div class="accent" style="width:100px"></div></div>
  <div class="abs tag" style="left:901px;top:38px">Your Logo</div>
  <div class="abs tag" style="left:558px;top:58px;color:var(--blue)">Pages&nbsp; 08</div>
  <div class="photo" role="img" aria-label="Small photo of a bathroom vanity" style="left:578px;top:205px;width:156px;height:148px;background:linear-gradient(180deg,#e6e6e6,#6a6d72)"></div>
  <div class="abs anton" style="left:759px;top:207px;font-size:19px;color:var(--blue)">CONVALLIS JUSTOO</div>
  <div class="abs" style="left:759px;top:238px;font-size:10px;font-weight:700;font-style:italic">Magna Lobortisr</div>
  <div class="abs body-copy" style="left:759px;top:262px;width:210px">Integer sed eleifend massa. Suspendisse hendrerit purus ac magna lobortis, sit amet convallis justo sagittis. Sed non dui libero. Quisque et sagittis ex, et dapibus mi. Maecenas eu faucibus leo.</div>
  <div class="abs" style="left:578px;top:376px;width:379px;height:1px;background:#9fc6e8"></div>
  <div class="abs anton" style="left:578px;top:404px;font-size:27px;line-height:1.45;color:var(--blue)">Our Vision ,<br>Mission And<br>Value</div>
  <div class="abs body-copy" style="left:759px;top:402px;width:210px">Phasellus ut accumsan purus. Nam malesuada lorem a velit pretium pellentesque eget eget magna. Aenean non massa lacinia, laoreet lacus nec, placerat velit. Proin tincidunt, magna et fermentum posuere, turpis velit pulvinar odio, volutpat pulvinar velit lorem sed ex.</div>
  <div class="abs body-copy" style="left:759px;top:520px;width:210px">Proin dictum arcu eu felis efficitur, ut iaculis risus accumsan. Donec odio arcu tempor eu imperdiet facilisis, pretium eget velit. Ut egestas nulla nibh, nec consectetur risus sagittis sit amet. Sed maximus, arcu nec porttitor mattis elit. Donec nec nisi arcu.</div>
</section>

<!-- Spread: quote -->
<section class="page" style="left:90px;top:2756px;width:1004px;height:704px">
  <div class="abs" style="left:5px;top:5px;width:994px;height:694px;background:var(--blue)"></div>
  <div class="abs" style="left:45px;top:47px;width:327px;height:2px;background:rgba(255,255,255,.6)"></div>
  <div class="abs" style="left:268px;top:46px;width:104px;height:4px;background:#fff"></div>
  <div class="abs tag" style="left:388px;top:41px;color:#fff">Your Logo</div>
  <div class="abs tag" style="left:45px;top:63px;color:#fff">Pages&nbsp; 06</div>
  <div class="abs" style="left:548px;top:47px;width:335px;height:2px;background:rgba(255,255,255,.6)"></div>
  <div class="abs" style="left:770px;top:46px;width:113px;height:4px;background:#fff"></div>
  <div class="abs tag" style="left:901px;top:41px;color:#fff">Your Logo</div>
  <div class="abs tag" style="left:548px;top:63px;color:#fff">Pages&nbsp; 07</div>
  <div class="abs" style="left:131px;top:127px;width:3px;height:517px;background:#fff"></div>
  <div class="abs" style="left:151px;top:207px;width:128px;font-size:10px;line-height:1.55;color:#fff;font-weight:500">Lorem ipsum dolor sit amet, consectetuer adipiscing elit, sed diam nonummy nibh euismod tincidunt ut laoreet dolore magna aliquam erat volutpat. Ut wisi enim ad minim veniam, quis nostrud exerci tation ullamcorper suscipit lobortis nisl ut aliquip ex ea commodo consequat. Duis autem vel eum iriure dolor in hendrerit in vulputate velit esse molestie consequat, vel illum dolore eu feugiat nulla facilisis at vero eros et accumsan et iusto odio dignissim qui blandit praesent luptatum zzril</div>
  <div class="abs" style="left:55px;top:650px;transform:rotate(-90deg);transform-origin:left top;color:#fff;white-space:nowrap;display:flex;align-items:baseline;gap:12px">
    <span style="font-size:18px">Subtitle</span><span class="anton" style="font-size:36px">HEADLINE HERE</span>
  </div>
  <div class="photo" role="img" aria-label="Photo of a white kitchen with range hood, open wooden shelves and a marble island" style="left:307px;top:134px;width:394px;height:536px;background:linear-gradient(180deg,#f2f2f0 0%,#d6d3ce 50%,#b9987a 100%)"></div>
  <div class="abs" style="left:701px;top:134px;width:296px;height:536px;background:linear-gradient(180deg,rgba(60,86,176,.92),var(--navy))"></div>
  <svg class="abs" style="left:690px;top:106px" width="60" height="52" viewBox="0 0 60 52" aria-hidden="true">
    <path d="M2 50 V26 Q2 4 24 0 V10 Q13 13 13 24 H26 V50 Z M34 50 V26 Q34 4 56 0 V10 Q45 13 45 24 H58 V50 Z" fill="#fff"/>
  </svg>
  <div class="abs" style="left:748px;top:236px;width:230px;font-size:29px;line-height:1.37;color:#fff;letter-spacing:.5px">Success isn’t just about what you ac-complish in your life; it’s about what you inspire others to do.</div>
</section>

</body>
</html>
```